House Church design model for faith-based organization

A design is needed for a house church model (Christian, faith-based). I’m looking for a graphic to convey four house church hallmarks showing the balance of member engagement. The four-part model includes - God’s Presence, Community, Discipleship, Outreach. The model should consist of the text for the four parts and the words - House Church

Perhaps a circular/modular design with House Church in the center. Using equally-sized interlocking slices or winged parts (graphically speaking, but not angelic wings) may help convey a balanced approach. It isn’t a process and should not appear in progressive steps, but the order (as listed) is used when explaining the concept. The model will be used for members to evaluate monthly focus.

I’m open to interpretation of the design and artwork. Designers should not feel a need to utilize cliché-like Christian symbols. However, if done minimally (and perhaps first century-like), they could be of interest (but are not required). Keeping it abstract may help readability and convey a roots/back-to-basics feel.

The artwork will be used for a video and PowerPoint presentation. It should be vector-based for simple movement/animation.

Additional thoughts:
Readable, not complex
Interesting interlocking design found at: https://www.plorvexia.com/circle-element-infographic-options-parts-steps-template-cycle-diagram-graph-round-chart-image572914386

Target Market(s)

To existing members (for reflection) and for those seeking a simpler church experience.

Requirements
Must have
• Simple, readable design, ability to reproduce for PowerPoint, video, and web. Prefer simple illustrations rather than images.
Nice to have
• The design should create a calming sense of focus on four priorities vs. the complexity of structure/requirements often found in the church experience.
Should not have
• Not crazy about puzzle pieces. Please avoid using all CAPS and serif fonts. Should not use complex images or photos.

```html
<!DOCTYPE html>
<html lang="en">
<head>
<meta charset="utf-8">
<title>House Church – Four Hallmarks</title>
<link rel="stylesheet" href="https://fonts.googleapis.com/css2?family=Poppins:wght@600&display=swap">
<style>
  :root {
    --bg: #ffffff;
    --presence-rim: #13a89e;
    --presence-fill: #1b9e8e;
    --community-rim: #8dc63f;
    --community-fill: #7cad43;
    --discipleship-rim: #ec4e40;
    --discipleship-fill: #d83b33;
    --outreach-rim: #f58526;
    --outreach-fill: #e07427;
    --hub-text: #2e3192;
    --label-text: #ffffff;
  }
  html, body {
    margin: 0;
    padding: 0;
    width: 1200px;
    height: 1200px;
    overflow: hidden;
    background: var(--bg);
  }
  .hallmark-model {
    display: block;
    width: 1200px;
    height: 1200px;
  }
  .petal--presence .petal__rim { fill: var(--presence-rim); }
  .petal--presence .petal__body { fill: var(--presence-fill); }
  .petal--community .petal__rim { fill: var(--community-rim); }
  .petal--community .petal__body { fill: var(--community-fill); }
  .petal--discipleship .petal__rim { fill: var(--discipleship-rim); }
  .petal--discipleship .petal__body { fill: var(--discipleship-fill); }
  .petal--outreach .petal__rim { fill: var(--outreach-rim); }
  .petal--outreach .petal__body { fill: var(--outreach-fill); }
  .petal-label {
    font-family: 'Poppins', sans-serif;
    font-weight: 600;
    font-size: 29px;
    fill: var(--label-text);
    letter-spacing: 0.5px;
  }
  .hub-label {
    font-family: 'Poppins', sans-serif;
    font-weight: 600;
    font-size: 40px;
    fill: var(--hub-text);
    text-anchor: middle;
  }
</style>
</head>
<body>
<svg class="hallmark-model" viewBox="0 0 1080 1080" xmlns="http://www.w3.org/2000/svg" role="img" aria-label="House Church model: God's Presence, Community, Discipleship, Outreach">
  <defs>
    <g id="petal-shape">
      <path class="petal__rim" d="M243 227 H448 A95 95 0 0 1 543 322 V430 A111 111 0 0 0 445 527 H338 A95 95 0 0 1 243 432 Z"/>
      <path class="petal__body" d="M267 251 H448 A71 71 0 0 1 519 322 V410 A135 135 0 0 0 426 503 H338 A71 71 0 0 1 267 432 Z"/>
    </g>
  </defs>

  <g class="petal petal--presence">
    <use href="#petal-shape"/>
  </g>
  <g class="petal petal--community" transform="translate(1112 0) scale(-1 1)">
    <use href="#petal-shape"/>
  </g>
  <g class="petal petal--discipleship" transform="translate(0 1080) scale(1 -1)">
    <use href="#petal-shape"/>
  </g>
  <g class="petal petal--outreach" transform="translate(1112 1080) scale(-1 -1)">
    <use href="#petal-shape"/>
  </g>

  <text class="petal-label" x="321" y="364">God’s</text>
  <text class="petal-label" x="321" y="403">Presence</text>
  <text class="petal-label" x="622" y="388">Community</text>
  <text class="petal-label" x="296" y="720">Discipleship</text>
  <text class="petal-label" x="648" y="719">Outreach</text>

  <text class="hub-label" x="560" y="532">House</text>
  <text class="hub-label" x="560" y="572">Church</text>
</svg>
</body>
</html>
```